Cannabis Company needs a packaging design for a 4x6 pouch

We need a design for a new cannabis company. Included is the logo in red. The logo color can change. Whatever color looks best with the design is what we'll use. The design can't include any cartoon characters or anything that may appeal to children. We have multiple products that are similar that will be using the same design. The pouch will contain 10 pyramid shaped gummies. The look we're going for is modern, simple, but eye catching. I included a handful of photos of packaging we like if that helps.

```html
<!DOCTYPE html>
<html lang="en">
<head>
<meta charset="utf-8">
<title>Verdalo Delta-8 THC Gummies – Blueberry Pouch</title>
<link rel="stylesheet" href="https://fonts.googleapis.com/css2?family=Bebas+Neue&family=Poppins:wght@400;600;700&family=Great+Vibes&display=swap">
<style>
  :root {
    --page: #ffffff;
    --pouch-top: #284a92;
    --pouch-mid: #3560b0;
    --pouch-low: #2a4f98;
    --berry-dark: #1e3466;
    --berry-mid: #3c5d9e;
    --white: #ffffff;
    --lime: #e8f000;
    --olive: #b0bd16;
    --navy: #1b2f5e;
    --divider: rgba(255,255,255,0.14);
  }
  * { margin: 0; padding: 0; box-sizing: border-box; }
  html, body { width: 1200px; height: 2400px; overflow: hidden; background: var(--page); }
  .canvas { position: relative; width: 1200px; height: 2400px; }
  .pouch-front {
    position: absolute; left: 0; top: 297px; width: 1200px; height: 1806px; overflow: hidden;
    background: linear-gradient(180deg, var(--pouch-top) 0%, var(--pouch-mid) 62%, var(--pouch-low) 100%);
    box-shadow: 0 14px 30px rgba(0,0,0,0.18);
  }
  .pattern-area {
    position: absolute; left: 0; top: 0; width: 100%; height: 900px;
    background: radial-gradient(ellipse at 50% 30%, rgba(255,255,255,0.04), rgba(0,0,0,0.06) 70%);
  }
  .berries-photo {
    position: absolute; left: 0; bottom: 0; width: 100%; height: 420px;
    background: linear-gradient(180deg, rgba(30,52,102,0) 0%, var(--berry-mid) 40%, var(--berry-dark) 100%);
  }
  .brand { position: absolute; left: 0; width: 100%; top: 560px; text-align: center; color: var(--white); }
  .brand-name { font-family: 'Poppins', sans-serif; font-weight: 600; font-size: 100px; line-height: 1; letter-spacing: -2px; }
  .brand-tagline { font-family: 'Poppins', sans-serif; font-weight: 400; font-size: 24px; letter-spacing: 6px; margin-top: 10px; }
  .product-title { position: absolute; left: 0; width: 100%; top: 790px; text-align: center; font-weight: 400; }
  .title-line { display: block; font-family: 'Bebas Neue', sans-serif; font-weight: 400; font-size: 186px; line-height: 1; color: var(--white); letter-spacing: 2px; }
  .title-accent { display: block; font-family: 'Poppins', sans-serif; font-weight: 700; font-size: 150px; line-height: 1; color: var(--lime); margin-top: -6px; letter-spacing: -2px; }
  .flavour { position: absolute; left: 0; width: 100%; top: 1060px; text-align: center; font-family: 'Great Vibes', cursive; font-size: 150px; line-height: 1; color: var(--white); }
  .claims { position: absolute; top: 1230px; left: 210px; width: 810px; display: flex; list-style: none; padding: 0; margin: 0; }
  .claim { flex: 1; list-style: none; text-align: center; color: var(--white); font-family: 'Poppins', sans-serif; font-weight: 400; font-size: 34px; line-height: 1.2; padding: 4px 0 14px; }
  .claim + .claim { border-left: 2px solid var(--divider); }
  .claim svg { display: block; margin: 0 auto 10px; }
  .dose-strip {
    position: absolute; left: 470px; top: 1600px; width: 440px; height: 48px; background: var(--lime);
    border-radius: 8px; font-family: 'Poppins', sans-serif; font-weight: 600; font-size: 26px; color: var(--navy);
    line-height: 48px; padding-left: 28px; white-space: nowrap;
  }
  .count-badge {
    position: absolute; left: 880px; top: 1518px; width: 200px; height: 200px; border-radius: 50%;
    background: var(--white); border: 6px solid var(--pouch-top); text-align: center; padding-top: 22px;
  }
  .count-number { font-family: 'Poppins', sans-serif; font-weight: 700; font-size: 96px; line-height: 1; color: var(--navy); letter-spacing: -4px; }
  .count-label { font-family: 'Bebas Neue', sans-serif; font-size: 46px; line-height: 1; color: var(--olive); }
</style>
</head>
<body>
<main class="canvas">
  <section class="pouch-front">
    <div class="pattern-area" role="img" aria-label="Faint line-drawn pattern of blueberries and leaves"></div>
    <div class="berries-photo" role="img" aria-label="Photograph of fresh blueberries scattered along the bottom"></div>

    <div class="brand">
      <div class="brand-name">verdalo</div>
      <div class="brand-tagline">CANNABIS COMPANY</div>
    </div>

    <h1 class="product-title">
      <span class="title-line">DELTA-8 THC</span>
      <span class="title-accent">GUMMIES</span>
    </h1>
    <div class="flavour">Blueberry</div>

    <ul class="claims">
      <li class="claim">
        <svg width="58" height="58" viewBox="0 0 58 58" fill="none" stroke="#e8f000" stroke-width="3"><circle cx="29" cy="29" r="25"/><path d="M29 14v30M22 20l7 6 7-6M22 29l7 6 7-6"/><path d="M13 45 45 13"/></svg>
        Gluten Free
      </li>
      <li class="claim">
        <svg width="58" height="58" viewBox="0 0 58 58" fill="none" stroke="#e8f000" stroke-width="3"><circle cx="29" cy="29" r="25"/><text x="29" y="35" text-anchor="middle" font-family="Poppins, sans-serif" font-size="15" font-weight="700" fill="#e8f000" stroke="none">GMO</text><path d="M13 45 45 13"/></svg>
        Non GMO
      </li>
      <li class="claim">
        <svg width="58" height="58" viewBox="0 0 58 58" fill="none" stroke="#e8f000" stroke-width="3"><circle cx="29" cy="29" r="25"/><path d="M29 15c-7 10-11 15-11 20a11 11 0 0 0 22 0c0-5-4-10-11-20z"/><path d="M13 45 45 13"/></svg>
        Fat Free
      </li>
    </ul>

    <div class="dose-strip">25MG DELTA 10 PER GUMMY</div>
    <div class="count-badge">
      <div class="count-number">10</div>
      <div class="count-label">GUMMIES</div>
    </div>
  </section>
</main>
</body>
</html>
```